Buff Works Business card design

i need a business card design for my new detailing company called 'Brent's Detail Shop'. i want an all black and white design . simple, direct and to the point. i want the designer to choose a fitting font to match the logothe front should have logo, address, phone and email and the back side should have a slogan and text indicating that we offer services on anything including cars, trucks, motorcycles and RVs. slogan will read "we take pride in your ride"
maybe also very small on the back side the IG icon with Brents_Detail_Shop

phone 208.474.2863
address 3847 E Larkmoor Ave
Spokane WA 98734
email: BrentsDetail@quorvamail.com

Target Market(s)

all ages , auto enthusiasts

Industry/Entity Type

Automotive

Contact Information for Business Card

the front should have logo, address, phone and email and the back side should have a slogan and text indicating that we offer services on anything including cars, trucks, motorcycles and RVs. slogan will read "we take pride in your ride"

phone 208.474.2863
address 3847 E Larkmoor Ave
Spokane WA 98734

Colors
000000
ffffff

Requirements
Must have
• bold font and very simple design with good spacing
Nice to have
• anything creative from the designer indicating we service any types of vehicles
Should not have
• any colors ,

```html
<!DOCTYPE html>
<html lang="en">
<head>
<meta charset="utf-8">
<title>Brent's Detail Shop – Business Cards</title>
<link rel="stylesheet" href="https://fonts.googleapis.com/css2?family=Montserrat:wght@300;400;700&display=swap">
<style>
  :root {
    --ink: #0b0b0b;
    --paper: #f2f2f0;
    --white: #ffffff;
    --stage: #d9d6d2;
    --muted-light: #bdbdbd;
    --muted-dark: #555555;
    --rule: #dcdcda;
  }
  * { box-sizing: border-box; margin: 0; padding: 0; }
  html, body { width: 1200px; height: 1200px; overflow: hidden; }
  body {
    background: var(--stage);
    font-family: "Montserrat", sans-serif;
    position: relative;
  }
  .card {
    position: absolute;
    width: 660px;
    height: 377px;
    border-radius: 4px;
    box-shadow: 0 18px 40px rgba(0,0,0,.22);
  }

  /* Back side */
  .card-back {
    left: 90px; top: 120px;
    background: radial-gradient(ellipse at 50% 35%, #1d1d1d, var(--ink) 75%);
    color: var(--white);
    display: flex; flex-direction: column; align-items: center;
    padding-top: 30px;
  }
  .brand-mark {
    display: flex; align-items: center; gap: 10px;
    font-weight: 700; font-size: 20px; letter-spacing: .5px;
  }
  .brand-dot {
    width: 18px; height: 18px; border-radius: 50%;
    background: currentColor;
  }
  .slogan { margin-top: 28px; font-weight: 700; font-size: 22px; }
  .owner-name { margin-top: 12px; font-weight: 700; font-size: 32px; }
  .owner-role { font-weight: 300; font-size: 15px; color: var(--muted-light); margin-top: 2px; }
  .services {
    margin-top: 26px;
    width: 470px;
    border: 1px solid #8a8a8a;
    position: relative;
    padding: 22px 0 14px;
    text-align: center;
  }
  .services-label {
    position: absolute; top: -10px; left: 50%;
    transform: translateX(-50%);
    background: #0e0e0e; padding: 0 10px;
    font-weight: 300; font-size: 14px; color: var(--muted-light);
  }
  .services-list {
    list-style: none; display: flex; justify-content: center; gap: 22px;
    font-weight: 300; font-size: 17px;
  }
  .services-list li::before { content: "•"; margin-right: 6px; }
  .social {
    margin-top: 10px;
    display: flex; justify-content: center; align-items: center; gap: 6px;
    font-weight: 300; font-size: 10px; color: var(--muted-light);
  }
  .social-dot {
    width: 14px; height: 14px; border-radius: 50%;
    border: 1.5px solid var(--white);
  }

  /* Front side */
  .card-front {
    left: 450px; top: 650px;
    background: var(--paper);
    color: var(--ink);
    display: flex;
  }
  .front-logo {
    width: 50%;
    display: flex; align-items: center; justify-content: center;
    border-right: 1px solid var(--rule);
  }
  .front-logo .brand-mark { font-size: 24px; }
  .front-logo .brand-dot { width: 22px; height: 22px; }
  .front-info { width: 50%; padding: 56px 0 0 34px; }
  .contact-name { font-weight: 700; font-size: 30px; }
  .contact-role { font-weight: 400; font-size: 14px; color: var(--muted-dark); margin-top: 2px; }
  .address { margin-top: 32px; font-weight: 400; font-size: 15px; line-height: 1.5; }
  .contact-line {
    display: flex; align-items: center; gap: 10px;
    margin-top: 8px; font-size: 15px;
  }
  .contact-line svg { width: 15px; height: 15px; flex: none; }
  .address + .contact-line { margin-top: 10px; }
</style>
</head>
<body>

<section class="card card-back" aria-label="Business card back">
  <div class="brand-mark"><span class="brand-dot"></span>Brent's Detail Shop</div>
  <p class="slogan">We take pride in your ride</p>
  <h2 class="owner-name">Dale Morrow</h2>
  <p class="owner-role">Owner</p>
  <div class="services">
    <span class="services-label">Our Service</span>
    <ul class="services-list">
      <li>Cars</li><li>Trucks</li><li>Motorcycles</li><li>RVs</li>
    </ul>
    <div class="social"><span class="social-dot"></span>Brents_Detail_Shop</div>
  </div>
</section>

<section class="card card-front" aria-label="Business card front">
  <div class="front-logo">
    <div class="brand-mark"><span class="brand-dot"></span>Brent's Detail Shop</div>
  </div>
  <div class="front-info">
    <h2 class="contact-name">Kyle Banner</h2>
    <p class="contact-role">General Manager</p>
    <p class="address">3847 E Larkmoor Ave<br>Spokane WA 98734</p>
    <p class="contact-line">
      <svg viewBox="0 0 24 24" aria-hidden="true"><path fill="currentColor" d="M6.6 10.8a15.1 15.1 0 0 0 6.6 6.6l2.2-2.2a1 1 0 0 1 1-.25 11.4 11.4 0 0 0 3.6.57 1 1 0 0 1 1 1V20a1 1 0 0 1-1 1A17 17 0 0 1 3 4a1 1 0 0 1 1-1h3.5a1 1 0 0 1 1 1c0 1.25.2 2.46.57 3.6a1 1 0 0 1-.25 1z"/></svg>
      208.474.2863
    </p>
    <p class="contact-line">
      <svg viewBox="0 0 24 24" aria-hidden="true"><path fill="currentColor" d="M2 5h20v14H2z"/><path fill="none" stroke="var(--paper)" stroke-width="1.8" d="M2.5 5.5 12 13l9.5-7.5"/></svg>
      BrentsDetail@quorvamail.com
    </p>
  </div>
</section>

</body>
</html>
```